Eye catching while remaining subtle, stylish and professional

Pellmore Works are a Heatpump and Air Conditioning Company. I would like stationary that would be suitable to use for letters, quoting invoicing. The final design should communicate a trade/service type industry that is clean and professional

I would like the designer to also offer a Business card option as well.

Details should include company logo as attached. Company details. Name, Address, Phone, Email and Website. You can use generic details until a final design is chosen

Target Market(s)

Trade/Service Industry

Industry/Entity Type

Air Conditioning

Requirements
Must have
• LOGO, Company contact details
Nice to have
• Watermark

```html
<!DOCTYPE html>
<html lang="en">
<head>
<meta charset="utf-8">
<title>Pellmore Works Stationery</title>
<link rel="stylesheet" href="https://fonts.googleapis.com/css2?family=Source+Sans+3:wght@400;600&family=Pinyon+Script&display=swap">
<style>
  :root {
    --backdrop: #3b3b3d;
    --paper: #ffffff;
    --brand-blue: #16a8df;
    --brand-blue-light: #5fc6ee;
    --watermark: #eef6fb;
    --text-grey: #555a5e;
    --rule-grey: #c9cdd0;
    --script-grey: #8a8d90;
  }
  * { margin: 0; padding: 0; box-sizing: border-box; }
  html, body { width: 1200px; height: 806px; overflow: hidden; }
  body {
    position: relative;
    background: var(--backdrop);
    font-family: "Source Sans 3", "Myriad Pro", Arial, sans-serif;
    color: var(--text-grey);
  }
  .sheet {
    position: absolute;
    background: var(--paper);
    box-shadow: 0 3px 8px rgba(0,0,0,0.45);
    overflow: hidden;
  }
  .wordmark {
    position: absolute;
    font-weight: 600;
    color: var(--brand-blue);
    font-size: 22px;
    letter-spacing: 0;
    white-space: nowrap;
    line-height: 1;
  }
  .divider {
    position: absolute;
    width: 1px;
    background: var(--rule-grey);
  }
  .contact {
    position: absolute;
    font-size: 9px;
    line-height: 12.5px;
    color: var(--text-grey);
    white-space: nowrap;
  }
  .contact .line { display: flex; align-items: center; gap: 4px; }
  .contact svg { width: 8px; height: 8px; fill: var(--brand-blue); flex: none; }
  .watermark {
    position: absolute;
    border-radius: 50%;
    background: var(--watermark);
  }

  /* business card front */
  .card-front { left: 40px; top: 39px; width: 259px; height: 148px; border-radius: 9px; }
  .card-front .wordmark { left: 24px; top: 63px; font-size: 15px; }
  .card-front .divider { left: 142px; top: 45px; height: 56px; }
  .card-front .holder-name { position: absolute; left: 157px; top: 42px; font-size: 11px; font-weight: 600; color: var(--brand-blue); }
  .card-front .contact { left: 157px; top: 59px; font-size: 7px; line-height: 10px; }
  .card-front .contact svg { width: 6px; height: 6px; }
  .card-front .card-rule { position: absolute; left: 0; right: 0; top: 126px; height: 2px; background: #d8dcdf; }
  .card-front .card-band {
    position: absolute; left: 0; right: 0; bottom: 0; height: 18px;
    background: linear-gradient(var(--brand-blue-light), var(--brand-blue));
    color: #e6f6fd; font-size: 7px; letter-spacing: 1px; text-align: center; line-height: 18px;
  }

  /* business card back */
  .card-back { left: 312px; top: 39px; width: 260px; height: 148px; border-radius: 9px; background: var(--brand-blue); }
  .card-back .pattern { position: absolute; inset: 0; background: linear-gradient(135deg, #1cb0e6, #11a2da); }
  .card-back .wordmark { left: 0; right: 0; top: 56px; text-align: center; color: #ffffff; font-size: 19px; }
  .card-back .web { position: absolute; left: 0; right: 0; top: 90px; text-align: center; color: #dff4fc; font-size: 7px; letter-spacing: 1.5px; }

  /* envelope */
  .envelope { left: 31px; top: 207px; width: 547px; height: 316px; }
  .envelope .flap {
    position: absolute; left: 0; top: 0; width: 100%; height: 79px;
    background: var(--brand-blue); border-radius: 12px 12px 0 0;
  }
  .envelope .flap-web {
    position: absolute; left: 0; right: 0; top: 21px; text-align: center;
    color: #e3f5fd; font-size: 7px; letter-spacing: 1px; transform: rotate(180deg);
  }
  .envelope .flap-dot { position: absolute; left: 259px; top: 40px; width: 22px; height: 22px; border-radius: 50%; background: #ffffff; }
  .envelope .wordmark { left: 27px; top: 108px; font-size: 21px; }
  .envelope .contact { left: 39px; top: 150px; font-size: 8px; line-height: 11px; }
  .envelope .watermark { left: 328px; top: 106px; width: 200px; height: 200px; }

  /* compliment slip */
  .compliment-slip { left: 31px; top: 540px; width: 547px; height: 238px; }
  .compliment-slip .wordmark { left: 32px; top: 44px; font-size: 17px; }
  .compliment-slip .divider { left: 163px; top: 27px; height: 56px; }
  .compliment-slip .contact { left: 177px; top: 25px; }
  .compliment-slip .watermark { left: 322px; top: 20px; width: 202px; height: 202px; }
  .compliment-slip .script-greeting {
    position: absolute; left: 34px; top: 168px;
    font-family: "Pinyon Script", "Times New Roman", cursive;
    font-size: 30px; color: var(--script-grey);
  }

  /* letterhead */
  .letterhead { left: 601px; top: 39px; width: 574px; height: 740px; }
  .letterhead .wordmark { left: 44px; top: 50px; font-size: 26px; }
  .letterhead .divider { left: 418px; top: 33px; height: 66px; }
  .letterhead .contact { left: 434px; top: 30px; }
  .letterhead .watermark { left: 152px; top: 248px; width: 254px; height: 254px; }
</style>
</head>
<body>

<svg width="0" height="0" style="position:absolute">
  <defs>
    <symbol id="icon-phone" viewBox="0 0 10 10"><path d="M1 3.5C1 2 2.5 1 5 1s4 1 4 2.5L7.5 4 7 3H3L2.5 4zM3 4.5h4l1.5 4.5h-7z"/></symbol>
    <symbol id="icon-mail" viewBox="0 0 10 10"><path d="M0.5 2h9v6h-9zM1.3 2.6 5 5.5l3.7-2.9z" fill-rule="evenodd"/></symbol>
    <symbol id="icon-web" viewBox="0 0 10 10"><circle cx="5" cy="5" r="4.5"/></symbol>
  </defs>
</svg>

<section class="sheet card-front">
  <div class="wordmark">Pellmore Works</div>
  <div class="divider"></div>
  <div class="holder-name">Alan Reed</div>
  <div class="contact">
    <div>Suite 102 Street name</div>
    <div>State, Zip 2034,Country</div>
    <div class="line" style="margin-top:3px"><svg><use href="#icon-phone"/></svg>127 345 9876</div>
    <div class="line"><svg><use href="#icon-mail"/></svg>info@yourname.com</div>
  </div>
  <div class="card-rule"></div>
  <div class="card-band">www.yourweb.com</div>
</section>

<section class="sheet card-back">
  <div class="pattern" role="img" aria-label="Repeating pattern of pale blue rings across the card back"></div>
  <div class="wordmark">Pellmore Works</div>
  <div class="web">www.yourweb.com</div>
</section>

<section class="sheet envelope">
  <div class="flap">
    <div class="flap-web">www.yourweb.com</div>
    <div class="flap-dot"></div>
  </div>
  <div class="wordmark">Pellmore Works</div>
  <div class="contact">
    <div>Suite 102 Street name</div>
    <div>State, Zip 2034, Country</div>
  </div>
  <div class="watermark"></div>
</section>

<section class="sheet compliment-slip">
  <div class="watermark"></div>
  <div class="wordmark">Pellmore Works</div>
  <div class="divider"></div>
  <div class="contact">
    <div>Suite 102 Street name</div>
    <div>State, Zip 2034,Country</div>
    <div class="line" style="margin-top:4px"><svg><use href="#icon-phone"/></svg>127 345 9876</div>
    <div class="line"><svg><use href="#icon-mail"/></svg>info@yourname.com</div>
    <div class="line"><svg><use href="#icon-web"/></svg>www.yourweb.com</div>
  </div>
  <div class="script-greeting">With Compliments</div>
</section>

<section class="sheet letterhead">
  <div class="watermark"></div>
  <div class="wordmark">Pellmore Works</div>
  <div class="divider"></div>
  <div class="contact">
    <div>Suite 102 Street name</div>
    <div>State, Zip 2034,Country</div>
    <div class="line" style="margin-top:5px"><svg><use href="#icon-phone"/></svg>127 345 9876</div>
    <div class="line"><svg><use href="#icon-mail"/></svg>info@yourname.com</div>
    <div class="line"><svg><use href="#icon-web"/></svg>www.yourweb.com</div>
  </div>
</section>

</body>
</html>
```